High end Electrical/home automation Business Card

Need a card for a high end electrical and home automation company utilising the existing logo.
Phone
Email
Website

Like black look with raised detail. Don’t necessarily need to keep colour of logo it could be made grayscale or white etc

Target Market(s)

High end clients

Contact Information for Business Card

Ridgeline Electrical

Requirements
Must have
• Logo, phone, email, website, address

High end look
Nice to have
• Black background card
Raised font
Should not have
• Lots of colour

```html
<!DOCTYPE html>
<html lang="en">
<head>
<meta charset="utf-8">
<title>Ridgeline Electrical – Business Card</title>
<link rel="stylesheet" href="https://fonts.googleapis.com/css2?family=Montserrat:wght@500;600;700&family=Work+Sans:wght@400;500&display=swap">
<style>
  :root {
    --backdrop: #1c1d1f;
    --card-dark: #3b3c3f;
    --card-dark-text: #56575b;
    --card-light: #ffffff;
    --ink: #333438;
    --ink-soft: #4a4b4f;
    --accent: #1a8fdb;
  }
  * { margin: 0; padding: 0; box-sizing: border-box; }
  html, body { width: 1200px; height: 852px; overflow: hidden; }
  body {
    background: var(--backdrop);
    display: flex;
    flex-direction: column;
    align-items: center;
    justify-content: center;
    gap: 40px;
    font-family: "Work Sans", sans-serif;
  }
  .card {
    position: relative;
    width: 600px;
    height: 343px;
    overflow: hidden;
  }
  .card--front {
    background: var(--card-dark);
    display: flex;
    align-items: center;
    justify-content: center;
    gap: 14px;
  }
  .front-brand {
    font-family: "Montserrat", sans-serif;
    font-weight: 700;
    font-size: 34px;
    color: var(--card-dark-text);
    letter-spacing: -0.5px;
  }
  .front-mark {
    width: 22px; height: 22px;
    border-radius: 50%;
    background: var(--card-dark-text);
  }
  .card--back { background: var(--card-light); }
  .back-shapes { position: absolute; inset: 0; }
  .brand {
    position: absolute;
    left: 40px; top: 132px;
    display: flex; align-items: center; gap: 10px;
  }
  .brand-mark {
    width: 18px; height: 18px;
    border-radius: 50%;
    background: var(--accent);
  }
  .brand-name {
    font-family: "Montserrat", sans-serif;
    font-weight: 700;
    font-size: 25px;
    color: var(--ink);
    letter-spacing: -0.5px;
  }
  .person {
    position: absolute;
    right: 34px; top: 42px;
    text-align: right;
  }
  .person-name {
    font-family: "Montserrat", sans-serif;
    font-weight: 600;
    font-size: 21px;
    color: var(--accent);
    letter-spacing: 0.5px;
  }
  .person-role {
    font-size: 13px;
    color: var(--ink-soft);
    margin-top: 2px;
  }
  .address {
    position: absolute;
    right: 34px; top: 124px;
    text-align: right;
    font-size: 13px;
    line-height: 1.45;
    color: var(--ink);
  }
  .contact {
    position: absolute;
    left: 40px; top: 258px;
    list-style: none;
    font-size: 14px;
    line-height: 1.45;
    color: var(--ink);
  }
  .contact li { display: flex; align-items: center; gap: 8px; }
  .contact svg { width: 11px; height: 11px; fill: var(--accent); flex: none; }
</style>
</head>
<body>
  <section class="card card--front" aria-label="Card front">
    <span class="front-mark"></span>
    <span class="front-brand">Ridgeline Electrical</span>
  </section>

  <section class="card card--back" aria-label="Card back">
    <svg class="back-shapes" viewBox="0 0 600 343" aria-hidden="true">
      <rect x="591" y="40" width="9" height="30" fill="var(--accent)"/>
      <line x1="270" y1="108" x2="586" y2="108" stroke="var(--accent)" stroke-width="1"/>
      <line x1="40" y1="246" x2="270" y2="246" stroke="var(--accent)" stroke-width="1"/>
      <polygon points="0,343 0,330 400,330 396,343" fill="var(--ink-soft)"/>
      <polygon points="396,343 412,290 600,262 600,343" fill="var(--accent)"/>
    </svg>

    <div class="brand">
      <span class="brand-mark"></span>
      <span class="brand-name">Ridgeline Electrical</span>
    </div>

    <div class="person">
      <p class="person-name">DANIEL HARPER</p>
      <p class="person-role">Founder</p>
    </div>

    <address class="address" style="font-style:normal">
      418 Cedar Hollow Road<br>
      Maple Falls, WA 98266
    </address>

    <ul class="contact">
      <li><svg viewBox="0 0 12 12"><path d="M2 1h3l1 3-1.5 1a7 7 0 0 0 2.5 2.5L8 6l3 1v3a1 1 0 0 1-1 1A9 9 0 0 1 1 2a1 1 0 0 1 1-1z"/></svg>555 214 3870</li>
      <li><svg viewBox="0 0 12 12"><path d="M1 2h10v8H1z M1.6 2.6 6 6.4l4.4-3.8v-.6H1.6z" fill-rule="evenodd"/></svg>hello@ridgeline.com</li>
      <li><svg viewBox="0 0 12 12"><circle cx="6" cy="6" r="5"/><path d="M1 6h10M6 1v10" stroke="#fff" stroke-width="0.8"/></svg>ridgelineelectrical.com</li>
    </ul>
  </section>
</body>
</html>
```